Flyer/Poster to promote Bicycle Race

We need a flyer that promotes a bicycle race in downtown Denver. It need to inspire spectators to come watch and bicycle racers to come race. It benefits the Cedar Hollow Cycling Club is getting urban kids on bikes; sharing healthy lifestyle and values
. We want the colors to be the colors of the logo - blue & red. Community Partnerships must have their logos on the flyer. Flyer must be able to be printed in 8 1/2 x 11 and 11 x 17

Target Market(s)

Neighborhood residents, athletes, cyclists

Industry/Entity Type

Non Profit

Font styles to use
Serif
Sans Serif

Colors
0592cd
ec1f27

Requirements
Must have
• Sunday, July 31, 2016
• Schedule:
• • Racing starts at 7:00am
• • Fun Ride on the Race Course at 12pm
• • Expo & Festival 10am – 6pm
• A Bike Race for Amateurs and Professionals
• A Bike Race for the young, the old & everyone in the middle.
• Great for spectators. Hang out, watch the action & explore the Festival
• Grab a bite to eat & cheer on the racers as they fly around the corners
• Special activities for kids: Pelton Course, Barnaby the Goat & More!!
• Teodoro Vasquez WLMR Music Director and Afternoon by the Creekside host will be onsite!
• Start/Finish/Festival will be on Harlow St between 4th Ave & 6th Ave
• Net proceeds benefit the Cedar Hollow Cycling Club dedicated to getting urban youth on bikes; sharing healthy lifestyle and values
• Special thanks to the Pemberton Foundation for their ongoing support
• HARLOWLOOPRACE.COM

```html
<!DOCTYPE html>
<html lang="en">
<head>
<meta charset="utf-8">
<title>The Harlow St – Race Flyer</title>
<link href="https://fonts.googleapis.com/css2?family=Oswald:wght@500;700&family=Roboto+Condensed:ital,wght@0,400;0,700;1,400;1,700&display=swap" rel="stylesheet">
<style>
  :root{
    --race-blue:#0592cd;
    --sky-blue:#1aa9e8;
    --race-red:#ec1f27;
    --ink:#1d1d1d;
    --bar:#363636;
    --paper:#ffffff;
    --stage:#d9d9d9;
  }
  html,body{margin:0;padding:0;width:1200px;height:858px;overflow:hidden;background:var(--stage);}
  .flyer{
    position:absolute;left:308px;top:19px;width:672px;height:945px;
    transform:scale(0.868);transform-origin:0 0;
    overflow:hidden;background:var(--race-red);
    font-family:"Roboto Condensed",Arial,sans-serif;color:var(--paper);
    box-shadow:0 10px 30px rgba(0,0,0,.35);
  }
  .backdrop{position:absolute;inset:0;}
  .event-mark{position:absolute;left:30px;top:196px;}
  .event-mark__name{display:flex;align-items:center;gap:8px;font-family:"Oswald",sans-serif;font-weight:700;font-size:34px;line-height:1;color:var(--ink);}
  .event-mark__dot{width:14px;height:14px;background:var(--race-red);}
  .event-mark__tribute{margin-top:4px;background:var(--race-blue);color:var(--paper);font-size:10px;font-weight:700;padding:2px 6px;display:inline-block;letter-spacing:.3px;}
  .event-date{position:absolute;left:20px;top:330px;font-family:"Oswald",sans-serif;font-weight:500;font-size:38px;letter-spacing:.3px;}
  .schedule{position:absolute;left:25px;top:380px;width:355px;height:116px;}
  .schedule__card{position:absolute;inset:0;}
  .schedule__title{position:absolute;left:10px;top:2px;font-family:"Oswald",sans-serif;font-weight:500;font-size:23px;color:var(--race-red);}
  .schedule__list{position:absolute;left:10px;top:38px;margin:0;padding:0;list-style:none;}
  .schedule__list li{font-style:italic;font-size:19px;color:var(--race-red);line-height:23px;border-bottom:1.5px solid var(--race-red);width:320px;}
  .schedule__list li:last-child{border-bottom:none;}
  .schedule__list li::before{content:"•";font-style:normal;margin-right:10px;font-size:14px;}
  .highlights{position:absolute;left:25px;top:508px;width:335px;margin:0;padding:0;list-style:none;font-size:13px;line-height:15.5px;}
  .highlights li{position:relative;padding-left:13px;margin-bottom:7px;}
  .highlights li::before{content:"✓";position:absolute;left:0;top:0;font-size:12px;}
  .benefit{position:absolute;left:20px;top:780px;width:305px;margin:0;font-style:italic;font-size:15.5px;line-height:19px;}
  .partners-tag{position:absolute;left:452px;top:562px;width:178px;height:30px;background:var(--race-red);font-style:italic;font-size:17px;line-height:30px;text-align:center;}
  .partner{position:absolute;font-weight:700;color:var(--ink);white-space:nowrap;line-height:1;}
  .partner--blue{color:#23408e;}
  .partner--red{color:var(--race-red);}
  .partner--gold{color:#e5a31b;}
  .partner--purple{color:#5b2f8c;}
  .badge{position:absolute;}
  .thanks{position:absolute;left:380px;top:838px;width:270px;margin:0;text-align:center;color:var(--race-red);font-style:italic;font-weight:700;font-size:14.5px;line-height:19px;}
  .site-bar{position:absolute;left:0;top:887px;width:672px;height:44px;background:var(--bar);font-size:19px;letter-spacing:1px;text-align:center;line-height:44px;}
</style>
</head>
<body>
<main class="flyer">
  <svg class="backdrop" width="672" height="945" viewBox="0 0 672 945">
    <defs>
      <linearGradient id="crowd" x1="0" y1="0" x2="1" y2="1">
        <stop offset="0" stop-color="#8c8f94"/>
        <stop offset=".45" stop-color="#6d4f7a"/>
        <stop offset="1" stop-color="#3c3a44"/>
      </linearGradient>
      <linearGradient id="street" x1="0" y1="0" x2="0" y2="1">
        <stop offset="0" stop-color="#c9cbcf"/>
        <stop offset="1" stop-color="#6e6a66"/>
      </linearGradient>
    </defs>
    <rect x="0" y="0" width="672" height="520" fill="url(#crowd)" role="img" aria-label="Photo of a pack of racing cyclists in helmets riding toward the camera"/>
    <polygon points="0,115 235,212 0,300" fill="var(--sky-blue)"/>
    <polygon points="570,290 672,240 672,460" fill="var(--sky-blue)"/>
    <polygon points="0,210 672,430 672,945 0,945" fill="var(--race-red)"/>
    <polygon points="455,400 672,468 672,945 285,945" fill="var(--paper)"/>
    <polygon points="0,764 355,752 338,842 0,852" fill="var(--sky-blue)"/>
    <polygon points="340,752 355,752 348,778" fill="#0a6f9c"/>
    <circle cx="487" cy="350" r="100" fill="#b7e2f4"/>
    <circle cx="480" cy="330" r="100" fill="#d9776c"/>
    <circle cx="475" cy="316" r="99" fill="var(--paper)"/>
    <circle cx="475" cy="316" r="95" fill="url(#street)" role="img" aria-label="Photo of riders racing past a street sign between city buildings"/>
  </svg>

  <div class="event-mark">
    <div class="event-mark__name"><span>THE HARLOW ST</span><span class="event-mark__dot"></span></div>
    <div class="event-mark__tribute">IN MEMORY OF MIKE PEMBERTON</div>
  </div>

  <div class="event-date">Sunday, July 31, 2016</div>

  <section class="schedule">
    <svg class="schedule__card" width="355" height="116" viewBox="0 0 355 116"><polygon points="0,0 355,0 330,116 0,116" fill="var(--paper)"/></svg>
    <div class="schedule__title">Schedule:</div>
    <ul class="schedule__list">
      <li>Racing starts at 7:00am</li>
      <li>Fun Ride on the Race Course at 12pm</li>
      <li>Expo &amp; Festival 10am – 6pm</li>
    </ul>
  </section>

  <ul class="highlights">
    <li>A Bike Race for Amateurs and Professionals</li>
    <li>A Bike Race for the young, the old &amp; everyone in the middle.</li>
    <li>Great for spectators. Hang out, watch the action &amp; explore the Festival</li>
    <li>Grab a bite to eat &amp; cheer on the racers as they fly around the corners</li>
    <li>Special activities for kids: Pelton Course, Barnaby the Goat &amp; More!!</li>
    <li>Teodoro Vasquez WLMR Music Director and Afternoon by the Creekside host will be onsite!</li>
    <li>Start/Finish/Festival will be on Harlow St between 4th Ave &amp; 6th Ave</li>
  </ul>

  <p class="benefit">Net proceeds benefit the Cedar Hollow Cycling Club dedicated to getting urban youth on bikes; sharing healthy lifestyle and values</p>

  <div class="partners-tag">Community Partners</div>
  <div class="partner" style="left:410px;top:632px;font-size:18px;">SUMMITFUEL</div>
  <div class="partner partner--blue" style="left:518px;top:634px;font-size:14px;">VELO NINE</div>
  <div class="partner partner--red" style="left:596px;top:635px;font-size:13px;">APEXA</div>
  <svg class="badge" style="left:440px;top:668px" width="50" height="50"><circle cx="25" cy="25" r="25" fill="#a9a29a"/></svg>
  <div class="partner partner--gold" style="left:500px;top:686px;font-size:14px;">GOLDEN SPOKE</div>
  <svg class="badge" style="left:596px;top:670px" width="44" height="46"><rect width="44" height="46" fill="var(--race-red)"/></svg>
  <div class="partner partner--red" style="left:396px;top:761px;font-size:12px;">CEDAR HOLLOW</div>
  <svg class="badge" style="left:482px;top:746px" width="50" height="42"><rect width="50" height="42" fill="#111"/></svg>
  <div class="partner partner--purple" style="left:546px;top:761px;font-size:12px;">PEAKVIEW MEDIA</div>

  <p class="thanks">Special thanks to the Pemberton Foundation<br>for their ongoing support</p>

  <div class="site-bar">HARLOWLOOPRACE.COM</div>
</main>
</body>
</html>
```